Zielgruppe
Wir sind ein Reisebüro (online und offline) mit dem Schwerpunkt Pauschalflugreisen, individuelle Flugreisen sowie Kreuzfahrten. Unsere Zielgruppe ist bunt gemischt, eher aber mit etwas gehobeneren, der heutigen Zeit entsprechenden Ansprüchen. Es sind Kunden, die mehr Wert auf qualifizierte Beratung legen und nicht auf der "geiz ist geil" Schiene fahren.
Aufgabenstellung
Wir benötigen Briefpapier, Visitenkarten, Katalogaufkleber und Stempel mit typischen Angaben, auf dem Briefpapier inkl. der Bankverbindung.

```html
<!DOCTYPE html>
<html lang="de">
<head>
<meta charset="utf-8">
<title>FernKompass.de – Visitenkarten</title>
<link rel="stylesheet" href="https://fonts.googleapis.com/css2?family=Open+Sans:wght@400;600;700&display=swap">
<style>
  :root {
    --canvas-bg: #e7e6e4;
    --card-white: #ffffff;
    --card-dark: #2f2d2c;
    --brand-blue: #4a9fd8;
    --ink-dark: #2b2b2b;
    --ink-text: #333333;
    --logo-light: #f4f4f4;
    --card-shadow: 0 6px 18px rgba(0,0,0,0.18);
  }
  * { margin: 0; padding: 0; box-sizing: border-box; }
  html, body {
    width: 1200px; height: 873px; overflow: hidden;
    background: var(--canvas-bg);
    font-family: "Open Sans", Arial, sans-serif;
  }
  .canvas {
    position: relative; width: 1200px; height: 873px;
  }
  .card {
    position: absolute; top: 275px;
    width: 500px; height: 324px;
    box-shadow: var(--card-shadow);
    overflow: hidden;
  }
  /* Vorderseite */
  .card--front { left: 70px; background: var(--card-white); }
  .card--front .brand-name {
    position: absolute; left: 34px; top: 36px;
    font-weight: 700; font-size: 34px; letter-spacing: -0.5px;
    color: var(--ink-dark);
  }
  .contact {
    position: absolute; right: 40px; top: 138px;
    text-align: right; font-size: 15px; line-height: 22px;
    color: var(--ink-text);
  }
  .contact .company { font-weight: 600; margin-bottom: 2px; }
  .bottom-band {
    position: absolute; left: 0; bottom: 0; width: 100%; height: 22px;
    display: flex;
  }
  .bottom-band .band-blue { width: 28%; background: var(--brand-blue); }
  .bottom-band .band-dark { flex: 1; background: var(--ink-dark); }
  .step-blocks {
    position: absolute; right: 34px; bottom: 22px;
    display: flex; align-items: flex-end; gap: 10px;
  }
  .step-blocks span { display: block; background: var(--ink-dark); height: 16px; }
  .step-blocks .step-s { width: 18px; }
  .step-blocks .step-m { width: 32px; }
  .step-blocks .step-l { width: 60px; }
  /* Rückseite */
  .card--back {
    left: 630px; background: var(--card-dark);
    display: flex; align-items: center; justify-content: center;
  }
  .card--back .brand-name {
    font-weight: 700; font-size: 46px; letter-spacing: -0.5px;
    color: var(--logo-light);
  }
</style>
</head>
<body>
<main class="canvas">
  <section class="card card--front" aria-label="Visitenkarte Vorderseite">
    <div class="brand-name">FernKompass.de</div>
    <address class="contact" style="font-style: normal;">
      <div class="company">Brandauer &amp; Kessler GbR</div>
      <div>Lindenhofstr. 21</div>
      <div>D-65203 Talheim</div>
      <div>T: +49(0)000 - 482915</div>
      <div>F: +49(0)000 - 7310062</div>
      <div>E: service@fernkompass.de</div>
    </address>
    <div class="step-blocks" aria-hidden="true">
      <span class="step-s"></span><span class="step-m"></span><span class="step-l"></span>
    </div>
    <div class="bottom-band" aria-hidden="true">
      <div class="band-blue"></div><div class="band-dark"></div>
    </div>
  </section>

  <section class="card card--back" aria-label="Visitenkarte Rückseite">
    <div class="brand-name">FernKompass.de</div>
  </section>
</main>
</body>
</html>
```